KTV - FlowFest 2022 Tradfe show 10'Wx8' display

My company Calibrated Works & Supplies, inc. ( K.T.V) has a display booth at the 2022 Virginia flow fest water wastewater trade show next month and would like new backdrop art for our 10'x8' banner stand. our website is
www.ktv-oakdale.example and our company line card is attached to give an idea of what we do. We want the main takeaway from the artwork to let customers know we offer Pumps, Blowers, Motors , Drives & Repair Services for the Municipal water & wastewater industry. Needs this in a high res pdf.

```html
<!DOCTYPE html>
<html lang="en">
<head>
<meta charset="utf-8">
<title>KTV Booth Backdrop</title>
<link rel="stylesheet" href="https://fonts.googleapis.com/css2?family=Archivo+Black&family=Exo+2:wght@700&family=Poppins:wght@400;500;700;800&display=swap">
<style>
  :root{
    --page:#ffffff;
    --ink:#262627;
    --night:#2a2a2c;
    --night-deep:#1b1b1d;
    --royal:#1a4da0;
    --royal-deep:#16398a;
    --orange:#e2700f;
    --white:#ffffff;
    --tick:#e8731a;
  }
  *{box-sizing:border-box;margin:0;padding:0}
  html,body{width:789px;height:1200px;overflow:hidden;background:var(--page)}
  .canvas{position:relative;width:789px;height:1200px;background:var(--page)}
  .backdrop{
    position:absolute;left:24px;top:301px;
    width:1318px;height:1065px;
    transform:scale(0.5615);transform-origin:0 0;
    overflow:hidden;background:var(--night);
    font-family:"Poppins",sans-serif;
  }
  .backdrop-shapes{position:absolute;inset:0}
  .brand{position:absolute;left:72px;top:70px;display:flex;align-items:center;gap:18px}
  .brand-dot{width:34px;height:34px;border-radius:50%;background:var(--royal)}
  .brand-text{display:flex;flex-direction:column}
  .brand-name{font-weight:800;font-size:110px;line-height:1;color:var(--ink);letter-spacing:2px}
  .brand-sub{font-weight:700;font-size:17px;color:var(--ink);margin-top:4px}
  .headline{position:absolute;left:68px;top:260px;line-height:1}
  .headline-industrial{font-family:"Exo 2",sans-serif;font-weight:700;font-size:112px;color:var(--royal);letter-spacing:1px}
  .headline-municipal{font-weight:800;font-size:86px;color:var(--orange);margin-top:2px}
  .headline-fire{font-weight:700;font-size:96px;color:var(--ink);margin-top:-2px}
  .service-area{position:absolute;left:72px;top:562px;font-weight:500;font-size:23px;line-height:1.22;color:var(--ink)}
  .product-photo{position:absolute;left:640px;top:80px;width:610px;height:720px}
  .offer-title{position:absolute;left:84px;top:752px;font-weight:800;font-size:41px;color:var(--white);white-space:nowrap}
  .offer-title span{font-weight:500;color:var(--orange)}
  .offer-list{position:absolute;top:812px;list-style:none;font-weight:500;font-size:31px;color:var(--white);line-height:39px}
  .offer-list li{display:flex;align-items:center;gap:16px;white-space:nowrap}
  .offer-list svg{width:24px;height:24px;flex:none}
  .col-a{left:86px}
  .col-b{left:530px;top:810px}
  .col-c{left:946px;top:814px}
  .web-pill{
    position:absolute;left:305px;top:945px;width:742px;height:64px;
    border-radius:32px;background:var(--orange);
    display:flex;align-items:center;justify-content:center;
    font-family:"Archivo Black",sans-serif;font-size:40px;letter-spacing:3px;color:var(--white);
  }
</style>
</head>
<body>
<div class="canvas">
  <section class="backdrop">
    <svg class="backdrop-shapes" viewBox="0 0 1318 1065" width="1318" height="1065" aria-hidden="true">
      <defs>
        <linearGradient id="nightFade" x1="0" y1="0" x2="1" y2="1">
          <stop offset="0" stop-color="#333335"/>
          <stop offset="1" stop-color="#1c1c1e"/>
        </linearGradient>
      </defs>
      <rect width="1318" height="1065" fill="url(#nightFade)"/>
      <path d="M0,0 H975 C1090,20 1170,70 1176,150 L1180,330 C1080,420 950,510 760,580 C560,660 360,705 210,700 C90,695 20,660 0,640 Z" fill="#fff"/>
      <path d="M0,600 C10,660 80,705 210,716 C400,728 650,660 840,560 C920,520 960,480 990,440 C940,490 860,540 760,580 C560,660 360,700 210,690 C100,684 30,650 0,600 Z" fill="var(--royal)"/>
      <path d="M695,80 C820,30 1000,5 1100,30 C1150,45 1175,95 1176,150 C1160,95 1120,55 1060,45 C960,30 820,50 695,80 Z" fill="var(--royal-deep)"/>
    </svg>

    <div class="brand">
      <div class="brand-text">
        <span class="brand-name">KTV</span>
        <span class="brand-sub">Calibrated Works &amp; Supplies</span>
      </div>
      <span class="brand-dot"></span>
    </div>

    <h1 class="headline">
      <div class="headline-industrial">Industrial</div>
      <div class="headline-municipal">MUNICIPAL</div>
      <div class="headline-fire">FIRE</div>
    </h1>

    <p class="service-area">SERVICING VIRGINIA | NORTH CAROLINA |<br>MARYLAND | DELAWARE SINCE 1981</p>

    <svg class="product-photo" viewBox="0 0 610 720" role="img" aria-label="Photo of a black submersible pump standing behind a blue horizontal pump with motor">
      <defs>
        <linearGradient id="pumpTone" x1="0" y1="0" x2="0" y2="1">
          <stop offset="0" stop-color="#242426"/>
          <stop offset="0.55" stop-color="#2f4f8a"/>
          <stop offset="1" stop-color="#2070d0"/>
        </linearGradient>
      </defs>
      <path d="M340,10 H560 V470 L610,560 V690 H20 V430 L200,400 L340,380 Z" fill="url(#pumpTone)"/>
    </svg>

    <h2 class="offer-title">OUR PRODUCTS <span>AND SERVICES</span></h2>

    <ul class="offer-list col-a">
      <li><svg viewBox="0 0 24 24"><rect x="2" y="4" width="17" height="17" rx="3" fill="none" stroke="var(--tick)" stroke-width="2.5"/><path d="M6 12l4 4 11-12" fill="none" stroke="var(--tick)" stroke-width="3"/></svg>Pumps &amp; Systems</li>
      <li><svg viewBox="0 0 24 24"><rect x="2" y="4" width="17" height="17" rx="3" fill="none" stroke="var(--tick)" stroke-width="2.5"/><path d="M6 12l4 4 11-12" fill="none" stroke="var(--tick)" stroke-width="3"/></svg>Blowers &amp; Packages</li>
      <li><svg viewBox="0 0 24 24"><rect x="2" y="4" width="17" height="17" rx="3" fill="none" stroke="var(--tick)" stroke-width="2.5"/><path d="M6 12l4 4 11-12" fill="none" stroke="var(--tick)" stroke-width="3"/></svg>Dry Process</li>
    </ul>
    <ul class="offer-list col-b">
      <li><svg viewBox="0 0 24 24"><rect x="2" y="4" width="17" height="17" rx="3" fill="none" stroke="var(--tick)" stroke-width="2.5"/><path d="M6 12l4 4 11-12" fill="none" stroke="var(--tick)" stroke-width="3"/></svg>Skid Fabrication</li>
      <li><svg viewBox="0 0 24 24"><rect x="2" y="4" width="17" height="17" rx="3" fill="none" stroke="var(--tick)" stroke-width="2.5"/><path d="M6 12l4 4 11-12" fill="none" stroke="var(--tick)" stroke-width="3"/></svg>Motors &amp; Drives</li>
      <li><svg viewBox="0 0 24 24"><rect x="2" y="4" width="17" height="17" rx="3" fill="none" stroke="var(--tick)" stroke-width="2.5"/><path d="M6 12l4 4 11-12" fill="none" stroke="var(--tick)" stroke-width="3"/></svg>Process Monitoring</li>
    </ul>
    <ul class="offer-list col-c">
      <li><svg viewBox="0 0 24 24"><rect x="2" y="4" width="17" height="17" rx="3" fill="none" stroke="var(--tick)" stroke-width="2.5"/><path d="M6 12l4 4 11-12" fill="none" stroke="var(--tick)" stroke-width="3"/></svg>Fire Protection</li>
      <li><svg viewBox="0 0 24 24"><rect x="2" y="4" width="17" height="17" rx="3" fill="none" stroke="var(--tick)" stroke-width="2.5"/><path d="M6 12l4 4 11-12" fill="none" stroke="var(--tick)" stroke-width="3"/></svg>Service &amp; Repair</li>
    </ul>

    <div class="web-pill">www.ktv-oakdale.example</div>
  </section>
</div>
</body>
</html>
```